Business cards - ZELTO Roofing & Siding

We need simple business cards made up for our Roofing & Siding business based in Calgary Alberta.
The logo on one side of the card and potentially our slogan "Built with trust, verified by time".
The other side could have:
-A small logo
-Rep name:
-Rep cell phone:
-Rep email:
-Office phone: 403-688-2904
-Website: PrairieTopCrafters.com

We would like to incorporate the colours from our logo, especially the lite blue on the jpeg file. I have attached the ai file and jpeg file. We like the colours better on the jpeg file.

```html
<!DOCTYPE html>
<html lang="en">
<head>
<meta charset="UTF-8">
<title>ZELTO Roofing &amp; Siding – Business Cards</title>
<link rel="stylesheet" href="https://fonts.googleapis.com/css2?family=Arimo:wght@400;700&display=swap">
<style>
  :root {
    --stage: #2b2e33;
    --card-white: #ffffff;
    --brand-blue: #3d7fd0;
    --brand-blue-deep: #2f6fc0;
    --brand-blue-light: #4d8ed8;
    --accent-red: #e0282e;
    --ink: #1d1d1f;
    --ink-soft: #2f3136;
  }
  * { margin: 0; padding: 0; box-sizing: border-box; }
  html, body {
    width: 1200px; height: 900px; overflow: hidden;
    background: var(--stage);
    font-family: "Arimo", Arial, sans-serif;
  }
  .sheet {
    position: relative; width: 1200px; height: 900px;
    display: flex; flex-direction: column; align-items: center; justify-content: center; gap: 60px;
  }
  .card {
    position: relative; width: 560px; height: 320px;
    box-shadow: 0 10px 28px rgba(0,0,0,.45);
    overflow: hidden;
  }

  /* Front: contact side */
  .card-front { background: var(--card-white); }
  .front-brand {
    position: absolute; left: 40px; top: 96px; width: 220px;
    display: flex; align-items: center; gap: 10px;
    color: var(--ink); font-weight: 700; font-size: 19px; line-height: 1.15;
  }
  .front-brand .brand-square {
    flex: none; width: 14px; height: 14px; background: var(--brand-blue);
  }
  .name-bar {
    position: absolute; left: 286px; top: 92px; width: 4px; height: 34px;
    background: var(--brand-blue);
  }
  .divider-red {
    position: absolute; left: 286px; top: 140px; width: 2px; height: 124px;
    background: var(--accent-red);
  }
  .rep {
    position: absolute; left: 304px; top: 90px; right: 20px;
  }
  .rep-name { color: var(--brand-blue); font-weight: 700; font-size: 25px; line-height: 1.05; }
  .rep-title { color: var(--ink-soft); font-size: 13px; margin-top: 5px; }
  .address { margin-top: 14px; color: var(--ink-soft); font-size: 13px; line-height: 1.3; }
  .contacts { list-style: none; margin-top: 10px; }
  .contacts li {
    display: flex; align-items: center; gap: 7px;
    color: var(--ink-soft); font-size: 13px; line-height: 1.4;
  }
  .contacts svg { width: 11px; height: 11px; flex: none; }

  /* Back: logo side */
  .card-back {
    background: linear-gradient(135deg, var(--brand-blue-light) 0%, var(--brand-blue) 55%, var(--brand-blue-deep) 100%);
    display: flex; align-items: center; justify-content: center;
  }
  .back-brand {
    display: flex; align-items: center; gap: 14px;
    color: var(--card-white); font-weight: 700; font-size: 30px; letter-spacing: .5px;
  }
  .back-brand .brand-square { width: 20px; height: 20px; background: var(--card-white); }
</style>
</head>
<body>
<main class="sheet">

  <section class="card card-front" aria-label="Business card front">
    <div class="front-brand">
      <span class="brand-square"></span>
      <span class="brand-name">ZELTO Roofing &amp; Siding</span>
    </div>

    <span class="name-bar"></span>
    <span class="divider-red"></span>

    <div class="rep">
      <h1 class="rep-name">Daniel Marrow</h1>
      <p class="rep-title">President and CEO</p>
      <p class="address">2418 - 9 Avenue S.E. Calgary<br>Alberta T2G 4K7</p>
      <ul class="contacts">
        <li>
          <svg viewBox="0 0 12 12" aria-hidden="true"><path d="M2.5 1 L4.5 1 L5.2 3.6 L4 4.6 C4.6 6 5.9 7.4 7.4 8 L8.4 6.8 L11 7.5 L11 9.5 C11 10.3 10.3 11 9.5 11 C5 11 1 7 1 2.5 C1 1.7 1.7 1 2.5 1 Z" fill="#e0282e"/></svg>
          403-688-2904
        </li>
        <li>
          <svg viewBox="0 0 12 12" aria-hidden="true"><rect x="0.5" y="2" width="11" height="8" rx="1" fill="#e0282e"/><path d="M1 2.6 L6 6.6 L11 2.6" fill="none" stroke="#fff" stroke-width="1"/></svg>
          info@prairietopcrafters.com
        </li>
        <li>
          <svg viewBox="0 0 12 12" aria-hidden="true"><circle cx="6" cy="6" r="5" fill="none" stroke="#e0282e" stroke-width="1.2"/><path d="M1 6 H11 M6 1 C3.5 3.5 3.5 8.5 6 11 M6 1 C8.5 3.5 8.5 8.5 6 11" fill="none" stroke="#e0282e" stroke-width="1"/></svg>
          PrairieTopCrafters.com
        </li>
      </ul>
    </div>
  </section>

  <section class="card card-back" aria-label="Business card back">
    <div class="back-brand">
      <span class="brand-square"></span>
      <span class="brand-name">ZELTO Roofing &amp; Siding</span>
    </div>
  </section>

</main>
</body>
</html>
```